Professional looking Roller Blind Discount Card that portrays quality at a value for money price!

We need a double sided business card designed as a discount card. Size 90mm wide x 55mm high.We would like it to look professional and portray quality at a value for money price point.I have uploaded a word document with a basic layout with the information we want included on each side of the card. Please put your own thought into the layout.

Contact Information for Business Card

As per word document attached.

```html
<!DOCTYPE html>
<html lang="en">
<head>
<meta charset="utf-8">
<title>K&amp;M Interiors – Roller Blinds Discount Card</title>
<link rel="stylesheet" href="https://fonts.googleapis.com/css2?family=Arimo:wght@400;700&family=Tinos&display=swap">
<style>
  :root {
    --canvas: #d4d5d7;
    --paper: #ffffff;
    --brand-blue: #27a4e0;
    --ink-grey: #6d6e70;
    --rule-grey: #8a8b8d;
    --blind-brown: #7d6a5f;
    --blind-brown-dark: #665449;
    --leaf-dark: #3f5a3a;
    --leaf-light: #9bb48c;
    --seal-gold: #f2b316;
    --seal-rim: #b57d0c;
    --white: #ffffff;
  }
  * { box-sizing: border-box; margin: 0; padding: 0; }
  html, body { width: 1200px; height: 900px; overflow: hidden; }
  body {
    background: var(--canvas);
    font-family: "Arimo", Arial, sans-serif;
    display: flex;
    align-items: center;
    justify-content: center;
    gap: 40px;
  }
  .card {
    position: relative;
    width: 540px;
    height: 330px;
    overflow: hidden;
    box-shadow: 0 6px 18px rgba(0,0,0,.18);
  }

  /* Front side */
  .card--front { background: var(--paper); }
  .front__brand {
    position: absolute; left: 40px; top: 40px;
    display: flex; align-items: center; gap: 12px;
    font-family: "Tinos", "Times New Roman", serif;
    font-size: 34px; letter-spacing: 1px;
    color: var(--brand-blue);
  }
  .front__brand-square {
    width: 14px; height: 14px; background: var(--brand-blue);
  }
  .front__offer {
    position: absolute; left: 40px; top: 108px;
    font-weight: 700; font-size: 40px; color: var(--brand-blue);
  }
  .front__details {
    position: absolute; left: 40px; top: 162px;
    font-size: 19px; line-height: 24px; color: var(--ink-grey);
  }
  .front__seals {
    position: absolute; left: 40px; top: 222px;
    display: flex; gap: 16px;
  }
  .seal {
    width: 40px; height: 40px; border-radius: 50%;
    background: radial-gradient(circle at 40% 35%, #ffd868, var(--seal-gold) 60%, var(--seal-rim));
  }
  .front__call {
    position: absolute; left: 40px; top: 278px;
    font-size: 20px; color: var(--ink-grey);
  }
  .front__call strong { color: var(--brand-blue); font-weight: 700; }
  .front__rule {
    position: absolute; left: 0; right: 0; bottom: 10px;
    height: 6px; background: var(--rule-grey);
  }

  /* Back side */
  .card--back { color: var(--white); }
  .back__photo {
    position: absolute; inset: 0;
    background: linear-gradient(180deg,
      var(--blind-brown) 0%, var(--blind-brown) 16%,
      var(--leaf-light) 28%, var(--leaf-dark) 52%, var(--leaf-light) 68%,
      var(--blind-brown) 74%, var(--blind-brown) 100%);
  }
  .back__brand {
    position: absolute; right: 28px; top: 18px;
    font-family: "Tinos", "Times New Roman", serif;
    font-size: 15px; letter-spacing: .5px;
  }
  .back__title {
    position: absolute; left: 0; right: 0; top: 56px;
    text-align: center;
    text-shadow: 0 0 3px rgba(0,0,0,.8), 1px 1px 2px rgba(0,0,0,.6);
  }
  .back__title-main { font-size: 50px; font-weight: 400; letter-spacing: 1px; }
  .back__title-sub { font-size: 30px; margin-top: 4px; }
  .back__band {
    position: absolute; left: 0; right: 0; bottom: 0; height: 86px;
    background: var(--blind-brown-dark);
    display: flex; flex-direction: column; justify-content: center;
    padding-left: 40px;
    transform: rotate(180deg);
  }
  .back__phone { font-weight: 700; font-size: 34px; letter-spacing: 2px; }
  .back__cta { font-size: 17px; letter-spacing: 1px; margin-top: 2px; }
</style>
</head>
<body>
  <section class="card card--front" aria-label="Card front">
    <div class="front__brand"><span class="front__brand-square"></span>K&amp;M INTERIORS</div>
    <div class="front__offer">25% OFF</div>
    <p class="front__details">Quality Custom Made Roller Blinds<br>Blockout • Screen • Light Filtering</p>
    <div class="front__seals">
      <span class="seal"></span><span class="seal"></span><span class="seal"></span>
    </div>
    <p class="front__call">Call <strong>0400 555 123</strong> Today!</p>
    <div class="front__rule"></div>
  </section>

  <section class="card card--back" aria-label="Card back">
    <div class="back__photo" role="img" aria-label="Photo of a room with brown roller blinds over windows looking onto a green garden"></div>
    <div class="back__brand">K&amp;M INTERIORS</div>
    <div class="back__title">
      <div class="back__title-main">ROLLER BLINDS</div>
      <div class="back__title-sub">Huge Selection of Fabrics</div>
    </div>
    <div class="back__band">
      <div class="back__phone">0400 555 123</div>
      <div class="back__cta">CALL TODAY!</div>
    </div>
  </section>
</body>
</html>
```